Eye-catching Card for new church

I would like a card the size of a business card ... that can be used to announce the start of our new church. I would like it to have our logo on the card, my name, and the statement "Coming Soon ... 1.10.2016". I also would like to list our website address and Facebook page and my Twitter account.

Target Market(s)

prospective people looking for a church

Industry/Entity Type

Church

Requirements
Must have
• a focus on Coming Soon ... 1.10.2016
• Brightfield Church logo
Should not have
• church buildings or writings on the cross

```html
<!DOCTYPE html>
<html lang="en">
<head>
<meta charset="utf-8">
<title>Brightfield Church – Coming Soon Card</title>
<link rel="stylesheet" href="https://fonts.googleapis.com/css2?family=EB+Garamond:wght@400;600;700&family=Pinyon+Script&display=swap">
<style>
  :root {
    --backdrop: #2a2a2c;
    --card-light: #f7f7f8;
    --card-mid: #e4e4e7;
    --card-shade: #d6d6da;
    --ink: #2b2b2e;
    --ink-soft: #4a4a4f;
    --brand-blue: #1f5aa6;
    --accent-blue: #2a7fc9;
    --icon-blue: #2457a3;
    --rule: #55555a;
  }
  * { box-sizing: border-box; margin: 0; padding: 0; }
  html, body {
    width: 1200px; height: 873px; overflow: hidden;
    background: var(--backdrop);
  }
  .stage {
    width: 1200px; height: 873px;
    display: flex; align-items: center; justify-content: center;
  }
  .card {
    position: relative;
    width: 960px; height: 548px;
    border-radius: 34px;
    overflow: hidden;
    box-shadow: 0 18px 40px rgba(0,0,0,0.45);
  }
  .card__texture {
    position: absolute; inset: 0;
    background:
      linear-gradient(135deg, var(--card-light) 0%, var(--card-mid) 38%, var(--card-light) 62%, var(--card-shade) 100%);
  }
  .card__front {
    position: relative; height: 100%;
    display: grid; grid-template-columns: 440px 1fr;
  }

  /* Left column: identity and contacts */
  .identity {
    padding: 92px 0 0 60px;
    font-family: "EB Garamond", Georgia, serif;
  }
  .brand {
    display: flex; align-items: center; justify-content: center; gap: 18px;
    width: 340px; margin-left: 10px;
  }
  .brand__dot {
    flex: none;
    width: 46px; height: 46px; border-radius: 50%;
    background: var(--brand-blue);
  }
  .brand__name {
    font-size: 32px; font-weight: 600; letter-spacing: 3px;
    text-transform: uppercase; color: var(--ink); line-height: 1.15;
    text-align: left;
  }
  .pastor {
    margin: 84px 0 0 10px; width: 340px; text-align: center;
    font-size: 30px; font-weight: 700; color: var(--ink);
    text-transform: uppercase; letter-spacing: 0.5px;
  }
  .contacts { list-style: none; margin-top: 40px; }
  .contacts__item {
    display: flex; align-items: center; gap: 18px;
    height: 50px;
    font-size: 22px; color: var(--ink-soft);
  }
  .contacts__icon { width: 34px; height: 34px; flex: none; }

  /* Right column: announcement */
  .announcement {
    padding: 62px 40px 0 20px;
    text-align: center;
    font-family: "EB Garamond", Georgia, serif;
  }
  .announcement__flourish {
    display: flex; align-items: center; justify-content: center; gap: 8px;
  }
  .announcement__rule { width: 38px; height: 1.5px; background: var(--rule); }
  .announcement__ornament {
    width: 70px; height: 16px; border-radius: 8px;
    background: linear-gradient(90deg, rgba(42,127,201,0.15), rgba(31,90,166,0.45), rgba(42,127,201,0.15));
  }
  .announcement__title {
    margin-top: 14px;
    font-family: "Pinyon Script", cursive;
    font-size: 48px; color: var(--ink); line-height: 1;
  }
  .announcement__date {
    margin: 4px 0 14px;
    font-size: 28px; color: var(--ink);
  }
  .announcement__message {
    margin: 56px auto 0; width: 420px;
    font-size: 25px; line-height: 1.62;
    color: var(--brand-blue);
  }
</style>
</head>
<body>
<main class="stage">
  <article class="card">
    <div class="card__texture" role="img" aria-label="Soft white faceted geometric background"></div>
    <div class="card__front">
      <section class="identity">
        <div class="brand">
          <span class="brand__dot"></span>
          <span class="brand__name">Brightfield Church</span>
        </div>
        <h1 class="pastor">Evan Marsh</h1>
        <ul class="contacts">
          <li class="contacts__item">
            <svg class="contacts__icon" viewBox="0 0 34 34" aria-hidden="true">
              <circle cx="17" cy="17" r="17" fill="var(--icon-blue)"/>
              <path d="M9.5 11.5 h15 a1.5 1.5 0 0 1 1.5 1.5 v8 a1.5 1.5 0 0 1 -1.5 1.5 h-8 l-4 3.5 v-3.5 h-3 a1.5 1.5 0 0 1 -1.5 -1.5 v-8 a1.5 1.5 0 0 1 1.5 -1.5 z" fill="#fff"/>
            </svg>
            @MarshEv
          </li>
          <li class="contacts__item">
            <svg class="contacts__icon" viewBox="0 0 34 34" aria-hidden="true">
              <circle cx="17" cy="17" r="17" fill="var(--icon-blue)"/>
              <g fill="none" stroke="#fff" stroke-width="2.4" stroke-linecap="round">
                <path d="M15 19 l4 -4"/>
                <path d="M13.5 16.5 l-2.5 2.5 a3 3 0 0 0 4.2 4.2 l2.5 -2.5"/>
                <path d="M20.5 17.5 l2.5 -2.5 a3 3 0 0 0 -4.2 -4.2 l-2.5 2.5"/>
              </g>
            </svg>
            www.thebrightfieldchurch.com
          </li>
          <li class="contacts__item">
            <svg class="contacts__icon" viewBox="0 0 34 34" aria-hidden="true">
              <circle cx="17" cy="17" r="17" fill="var(--icon-blue)"/>
              <rect x="10.5" y="9.5" width="13" height="15" rx="1.5" fill="#fff"/>
              <g stroke="var(--icon-blue)" stroke-width="1.6" stroke-linecap="round">
                <path d="M13.5 14 h7"/>
                <path d="M13.5 17 h7"/>
                <path d="M13.5 20 h4.5"/>
              </g>
            </svg>
            /BrightfieldChurchNW.com
          </li>
        </ul>
      </section>

      <section class="announcement">
        <div class="announcement__flourish">
          <span class="announcement__rule"></span>
          <span class="announcement__ornament" role="img" aria-label="Blue scroll ornament"></span>
          <span class="announcement__rule"></span>
        </div>
        <h2 class="announcement__title">Coming Soon..</h2>
        <p class="announcement__date">1st-October-2016</p>
        <div class="announcement__flourish">
          <span class="announcement__rule"></span>
          <span class="announcement__ornament" role="img" aria-label="Blue scroll ornament"></span>
          <span class="announcement__rule"></span>
        </div>
        <p class="announcement__message">God has called Laura &amp; I to plant a church. We are thankful for the big vision that has been placed in our hearts &amp; have been busy with the practical things to make it happen.</p>
      </section>
    </div>
  </article>
</main>
</body>
</html>
```